Flyer-Design für Träger der Familienhilfe
Zielgruppe
Wir sind ein Träger der Familienhilfe und bieten Hilfen zur Erziehung an. Unsere Auftraggeber sind die Jugendämter in Hamburg. Unsere Zielgruppe sind Familien/Einzelpersonen in Krisensituationen.
Aufgabenstellung
Wir möchten, dass unser Logo in das Design integriert wird. Da wir hauptsächlich mit Behörden, Ämtern, Schulen etc. zusammenarbeiten, ist es wichtig, dass wir einen seriösen Eindruck machen.
Wir haben provisorisch selbst einen Flyer erstellt, in dem alle wichtigen Informationen sind. Daran können Sie sich orientieren.

```html
<!DOCTYPE html>
<html lang="de">
<head>
<meta charset="utf-8">
<title>Lumen – Soziale Dienste Flyer</title>
<link href="https://fonts.googleapis.com/css2?family=Dosis:wght@300;400;600;700&family=Ubuntu:wght@300;400&display=swap" rel="stylesheet">
<style>
:root{
  --green:#9bc43c;
  --green-dark:#8cb52f;
  --grey:#8a8a8a;
  --grey-text:#7d7d7d;
  --white:#ffffff;
  --frame:#444;
}
*{margin:0;padding:0;box-sizing:border-box}
html,body{width:848px;height:1200px;overflow:hidden;background:#fff}
body{position:relative;font-family:"Dosis",sans-serif;color:var(--grey-text)}
.sheet{position:absolute;left:50px;width:732px;height:518px;border:1px solid var(--frame);overflow:hidden;background:var(--white)}
.sheet--outside{top:62px}
.sheet--inside{top:609px}
.top-band{position:absolute;left:0;top:0;width:100%;height:10px;background:var(--green)}
.panel{position:absolute;top:0;height:100%}
.sheet--outside .panel--info{left:0;width:239px}
.sheet--outside .panel--contact{left:239px;width:247px;background:var(--green)}
.sheet--outside .panel--cover{left:486px;width:246px}
h2{font-weight:700;color:var(--green);font-size:12.5px;line-height:1.2}
p{font-weight:300;font-size:10px;line-height:12.5px}
.info-text{position:absolute;left:22px;top:47px;width:200px}
.info-text p{margin-top:4px}
.lang-list{list-style:none;margin:6px 0 6px 0}
.lang-list li{position:relative;padding-left:62px;color:var(--green);font-weight:300;font-size:10.5px;line-height:17.5px}
.lang-list li::before{content:"•";position:absolute;left:32px;font-size:8px}
.info-text h2.spaced{margin-top:12px}
.photo{position:absolute;left:0;width:100%}
.photo--teens{top:379px;height:139px;background:linear-gradient(to bottom,#ffffff 0%,#e9e6df 22%,#c9b7a0 55%,#7d6a62 100%)}
.contact-text{position:absolute;left:50px;top:146px;color:var(--white);font-weight:400;font-size:11.3px;line-height:18.5px}
.contact-text .gap{height:18.5px}
.contact-text strong{font-weight:700}
.cover-claim{position:absolute;left:0;width:100%;top:126px;text-align:center;font-family:"Ubuntu",sans-serif;font-weight:300;font-size:17px;line-height:21px;color:var(--grey)}
.brand{position:absolute;left:0;width:100%;top:225px;text-align:center}
.brand-mark{display:block;margin:0 auto 6px;width:22px;height:22px;border-radius:50%;background:var(--green)}
.brand-name{font-family:"Ubuntu",sans-serif;font-weight:400;font-size:44px;line-height:46px;color:var(--grey)}
.brand-sub{font-family:"Ubuntu",sans-serif;font-weight:400;font-size:20px;line-height:24px;color:var(--grey);margin-top:2px}
.cover-services{position:absolute;right:18px;top:326px;text-align:right;font-family:"Ubuntu",sans-serif;font-weight:300;font-size:16.5px;line-height:28px;color:var(--grey)}
.cover-web{position:absolute;left:0;width:100%;top:468px;text-align:center;font-weight:700;font-size:13px;color:var(--green)}
.col{position:absolute;top:0;height:100%}
.col--questions{left:0;width:246px}
.col--about{left:246px;width:247px}
.col--how{left:493px;width:239px}
.divider{position:absolute;top:14px;height:342px;border-left:1px dashed #888}
.divider--a{left:246px}
.divider--b{left:493px}
.questions{position:absolute;left:19px;top:70px;width:210px}
.questions h3{font-weight:400;color:var(--green);font-size:12.5px;line-height:14.6px;margin-bottom:29px}
.col-text{position:absolute;top:23px}
.col--about .col-text{left:14px;width:220px}
.col--how .col-text{left:22px;width:200px}
.col-text p{margin-bottom:7px}
.col-text h2{margin:2px 0 3px}
.bullets{list-style:none;margin:4px 0 6px}
.bullets li{position:relative;padding-left:31px;font-weight:300;font-size:10px;line-height:12.5px;margin-bottom:7.5px}
.bullets li::before{content:"•";position:absolute;left:16px;font-size:7px}
.bullets--green li{color:var(--green);padding-left:31px;margin-bottom:0}
.bullets--green li::before{left:18px}
.col--how p{margin-bottom:5px}
.photo--figures{top:365px;height:153px;background:linear-gradient(to bottom,#ffffff 0%,#e7e2dc 25%,#c7a88a 55%,#9a8677 100%)}
</style>
</head>
<body>

<section class="sheet sheet--outside">
  <div class="top-band"></div>

  <div class="panel panel--info">
    <div class="info-text">
      <h2>Unsere Schwerpunkte</h2>
      <p>Sprachliche Vielfalt<br>Unsere Mitarbeiter*innen verfügen über unterschiedliche kulturelle und sprachliche Hintergründe.</p>
      <p style="margin-top:7px">Wir haben daher die Möglichkeit Ihnen auch auf</p>
      <ul class="lang-list">
        <li>Türkisch</li><li>Arabisch</li><li>Kurdisch</li><li>Englisch</li>
      </ul>
      <p>eine Betreuung anzubieten.</p>
      <h2 class="spaced">Psychische Erkrankungen</h2>
      <p style="margin-top:7px">Unsere Angebote richten sich auch an Menschen mit psychischen Erkrankungen und/oder seelischen Behinderungen.</p>
      <p style="margin-top:7px">Wir verfügen in diesem Bereich über viel Erfahrung und arbeiten eng mit Psychologen und Psychiatern zusammen, um Ihnen eine umfangreiche Hilfe anbieten zu können.</p>
    </div>
    <div class="photo photo--teens" role="img" aria-label="Foto: Gruppe Jugendlicher mit Büchern an einer Wand"></div>
  </div>

  <div class="panel panel--contact">
    <div class="contact-text">
      Standort und Erreichbarkeit<br>
      Lumen - Soziale Dienste<br>
      Lindenhofweg 7<br>
      20099 Hamburg
      <div class="gap"></div>
      Telefon: 040 - 555 123 40<br>
      Fax: 040 - 555 123 39<br>
      Email: info@lumen-familienhilfe.de
      <div class="gap"></div>
      Ansprechpartnerin<br>
      Frau Clara Bergmann
      <div class="gap"></div>
      Sie finden uns auch Online unter:<br>
      <strong>www.lumen-familienhilfe.de</strong>
    </div>
  </div>

  <div class="panel panel--cover">
    <div class="cover-claim">Betreuung - Begleitung<br>Unterstützung</div>
    <div class="brand">
      <span class="brand-mark"></span>
      <div class="brand-name">Lumen</div>
      <div class="brand-sub">Soziale Dienste</div>
    </div>
    <div class="cover-services">Ambulante Hilfen<br>Sozialpädagogische Familienhilfe<br>und Erziehungsbeistandschaft</div>
    <div class="cover-web">www.lumen-familienhilfe.de</div>
  </div>
</section>

<section class="sheet sheet--inside">
  <div class="top-band"></div>
  <div class="divider divider--a"></div>
  <div class="divider divider--b"></div>

  <div class="col col--questions">
    <div class="questions">
      <h3>Brauchen Sie oder Ihre Familie<br>Hilfe im Alltag?</h3>
      <h3>Stecken Sie und/oder<br>Ihre Familie in einer Krise?</h3>
      <h3>Sind Konflikte für Sie oder Ihre Familie nicht zu lösen und sie stehen vor Problemen, bei denen Sie nicht mehr weiter wissen?</h3>
      <h3>Brauchen Sie Hilfe bei Angelegenheiten mit Behörden/Ämtern und Institutionen wie der Schule oder Kindergärten?</h3>
    </div>
  </div>

  <div class="col col--about">
    <div class="col-text">
      <h2>Wer wir sind</h2>
      <p>Lumen - Soziale Dienste ist ein Träger der Kinder- und Jugendhilfe und arbeitet nach dem Kinder- und Jugendhilferecht des Sozialgesetzbuches (SGB VIII).</p>
      <p>Wir leisten Hilfen zur Erziehung insbesondere die sozialpädagogische Familienhilfe und den Erziehungsbeistand.</p>
      <p>Unsere Hilfen bieten wir immer mit Wertschätzung, Respekt, Toleranz und Offenheit an. Diese Prinzipien sind uns sehr wichtig.</p>
      <p>Wir begleiten, beraten und unterstützen Sie in den jeweiligen Situationen und Herausforderungen.</p>
      <h2>Unsere Angebote</h2>
      <p>Die Sozialpädagogische Familienhilfe gemäß §31 SGB VIII wird ambulant angeboten. Dabei bieten wir Unterstützung</p>
      <ul class="bullets">
        <li>bei der Bewältigung von Alltagsproblemen,</li>
        <li>bei Konflikten und Krisen,</li>
        <li>im Kontakt mit Ämtern und Institutionen und</li>
        <li>im Umgang mit Kulturen und der eigenen kulturellen Identität.</li>
      </ul>
    </div>
  </div>

  <div class="col col--how">
    <div class="col-text">
      <p>Der Erziehungsbeistand gemäß §30 SGB VIII richtet sich gezielt an das Kind, an den Jugendlichen oder jungen Erwachsenen.</p>
      <p style="margin-bottom:0">Hierbei stehen im Fokus der Hilfe</p>
      <ul class="bullets bullets--green"><li>die Stärkung zur Selbsthilfe,</li><li>die Hilfe und Unterstützung in</li></ul>
      <p>alltäglichen Aufgaben,</p>
      <ul class="bullets bullets--green"><li>das Lösen von Problemen</li></ul>
      <p>und die Entwicklung von alternativen Handlungsmöglichkeiten bei Kon-flikten sowie</p>
      <ul class="bullets bullets--green"><li>der Aufbau einer sinnvollen</li></ul>
      <p>und selbständigen Freizeitgestaltung, Bildungsförderung und beruflicher Qualifizierung.</p>
      <h2>Wie Sie die Hilfen bekommen</h2>
      <p>Wenn Sie oder Ihre Familie Hilfe benötigen, dann wenden sie sich vorerst für ein Beratungsgespräch an das für Sie zu-ständige Jugendamt. Bei dem Gespräch wird mit Ihnen gemeinsam geschaut, welche Hilfen für Sie passend sind und Sie werden anschließend an die Einrichtungen weitergeleitet.<br>Für Fragen stehen wir Ihnen natürlich darüber hinaus jeder Zeit zur Verfügung.</p>
    </div>
  </div>

  <div class="photo photo--figures" role="img" aria-label="Foto: bunte Holzfiguren aus verschiedenen Kulturen, die sich an den Händen halten"></div>
</section>

</body>
</html>
```